Interior designer needs a gorgeous, chic business card design.

A new, small Interior Design firm needs a business card that is chic, contemporary and elegant. Nothing over the top. My interiors are contemporary classic with an elegant feel to them. I like to use quality finishes and products rather than follow the latest fads. Projects can be anything from Pre start selections, bathrooms, kitchens, bedrooms, custom upholstery, furniture, rugs and art etc. The final design should display quality and an achievable sense of chic. I am open to all colours including black but not limited to this.

```html
<!DOCTYPE html>
<html lang="en">
<head>
<meta charset="utf-8">
<title>Vela Interiors – Business Card</title>
<link href="https://fonts.googleapis.com/css2?family=Maven+Pro:wght@400;500;700&display=swap" rel="stylesheet">
<style>
  :root {
    --teal: #63c5b8;
    --teal-text: #5fc4b5;
    --teal-line: #4f9e93;
    --charcoal: #3b3b3d;
    --white: #ffffff;
    --paper: #eef0ef;
  }
  * { box-sizing: border-box; margin: 0; padding: 0; }
  html, body {
    width: 1017px;
    height: 1200px;
    overflow: hidden;
    background: var(--paper);
    font-family: "Maven Pro", "Helvetica Neue", Arial, sans-serif;
  }
  .canvas {
    width: 1017px;
    height: 1200px;
    display: flex;
    flex-direction: column;
    align-items: center;
    justify-content: center;
    gap: 56px;
  }
  .card {
    width: 880px;
    height: 503px;
    position: relative;
    overflow: hidden;
  }
  .card--front {
    background: var(--teal);
    display: flex;
    align-items: center;
    justify-content: center;
    gap: 48px;
  }
  .brand-square {
    width: 190px;
    height: 190px;
    background: var(--white);
  }
  .brand-name {
    color: var(--white);
    font-weight: 500;
    line-height: 0.95;
    letter-spacing: 2px;
  }
  .brand-name span { display: block; }
  .brand-name .brand-name__main { font-size: 122px; }
  .brand-name .brand-name__sub { font-size: 86px; }

  .card--back { background: var(--charcoal); }
  .back-mark {
    position: absolute;
    left: 40px;
    top: 60px;
  }
  .contact {
    position: absolute;
    left: 300px;
    top: 168px;
    color: var(--white);
  }
  .contact__name {
    color: var(--teal-text);
    font-weight: 700;
    font-size: 38px;
    letter-spacing: 2px;
    margin-bottom: 12px;
  }
  .contact__line {
    font-weight: 400;
    font-size: 27px;
    line-height: 1.33;
    letter-spacing: 0.5px;
  }
</style>
</head>
<body>
  <main class="canvas">
    <section class="card card--front" aria-label="Card front">
      <div class="brand-square"></div>
      <h1 class="brand-name">
        <span class="brand-name__main">VELA</span>
        <span class="brand-name__sub">INTERIORS</span>
      </h1>
    </section>

    <section class="card card--back" aria-label="Card back">
      <svg class="back-mark" width="220" height="380" viewBox="0 0 220 380" aria-hidden="true">
        <rect x="4" y="4" width="212" height="212" fill="none" stroke="var(--teal-line)" stroke-width="7"/>
      </svg>
      <div class="contact">
        <h2 class="contact__name">MARISA VELA HOLT</h2>
        <p class="contact__line">Dip. Interior Design</p>
        <p class="contact__line">Director</p>
        <p class="contact__line">0400555018</p>
        <p class="contact__line">marisa@velainteriors.com.au</p>
        <p class="contact__line">velainteriors.com</p>
      </div>
    </section>
  </main>
</body>
</html>
```